Web Design for ORV Air conditioning company

Hello,

I am calling on you for the modernization of the company's website
https://clim-solaris-atelier.fr/

The new one must include the new logo with the new graphic charter (color, style ...)

I'm looking for a simple design (less is more), a font written without Serif, the logo that brings a touch of color and modernity.

(maintenance and installation company for air conditioning and ventilation systems)
COLORS: in line with the logo

CHAPTER:

# PRESENTATION
# SERVICES
AIR CONDITIONING (ice cube icon)
HEATING (flame icon)
AIR TREATMENT (icon fan)
# ACHIEVEMENTS

# CONTACT
CONTACT FORM
GOOGLE MAPS

Target Market(s)

Showcase site for our customers

Coding

Coded - Design and coding required

Number of Pages Required

4 page

Font styles to use
Sans Serif

Colors
33b8a4
33a6d7
3176b5
ffffff

Requirements
Must have
• Clear and fluid navigation
a visual identity of the page with the logo
Should not have
• Overloaded.

```html
<!DOCTYPE html>
<html lang="en">
<head>
<meta charset="UTF-8">
<title>ORV — Air Conditioning &amp; Ventilation</title>
<link rel="stylesheet" href="https://fonts.googleapis.com/css2?family=Montserrat:wght@400;500;800&display=swap">
<style>
  :root {
    --sky: #46e6df;
    --white: #ffffff;
    --ink: #000000;
    --nav-ink: #0d2a3a;
    --brand-blue: #3476b8;
    --brand-teal: #33b8a4;
    --brand-cyan: #33a6d7;
    --logo-ink: #1f3a40;
  }
  * { margin: 0; padding: 0; box-sizing: border-box; }
  html, body { width: 1200px; height: 675px; overflow: hidden; }
  body { font-family: "Montserrat", Arial, sans-serif; background: var(--sky); }

  .hero { position: relative; width: 1200px; height: 675px; background: var(--sky); overflow: hidden; }

  .corner-panel { position: absolute; left: 0; top: 0; }

  .brand {
    position: absolute; left: 90px; top: 48px;
    display: flex; align-items: center; gap: 8px;
    font-weight: 800; font-size: 34px; letter-spacing: 1px;
    color: var(--logo-ink); line-height: 1;
  }
  .brand-mark { width: 12px; height: 12px; background: var(--brand-teal); }

  .main-nav {
    position: absolute; top: 52px; left: 0; width: 1200px; height: 22px;
    font-size: 16px; font-weight: 400; color: var(--nav-ink);
  }
  .main-nav a { position: absolute; color: inherit; text-decoration: none; white-space: nowrap; line-height: 22px; }
  .nav-home { left: 648px; }
  .nav-about { left: 750px; }
  .nav-services { left: 872px; display: flex; align-items: center; gap: 6px; }
  .nav-contact { left: 1029px; }

  .hero-title {
    position: absolute; left: 92px; top: 219px;
    font-weight: 800; font-size: 70px; line-height: 62.5px;
    letter-spacing: -2.5px; color: var(--ink);
  }
  .hero-tagline {
    position: absolute; left: 97px; top: 427px;
    font-size: 19px; font-weight: 500; color: var(--ink); letter-spacing: 0.1px;
  }

  .btn {
    position: absolute; top: 485px; width: 181px; height: 46px;
    display: flex; align-items: center; justify-content: center;
    font-size: 19px; font-weight: 400; text-decoration: none;
  }
  .btn-contact { left: 92px; background: var(--brand-blue); color: var(--white); }
  .btn-services { left: 297px; background: var(--white); color: var(--ink); }

  .hero-photo {
    position: absolute; left: 603px; top: 103px; width: 547px; height: 572px;
    background: radial-gradient(ellipse at 55% 60%, #e9eef2 0%, #c4d3dc 35%, #3f6fc4 60%, rgba(70,230,223,0) 80%);
  }
</style>
</head>
<body>
  <main class="hero">
    <svg class="corner-panel" width="341" height="158" viewBox="0 0 341 158" aria-hidden="true">
      <polygon points="0,0 341,0 199,65 199,106 114,106 0,158" fill="#ffffff"/>
    </svg>

    <div class="brand"><span class="brand-mark"></span>ORV</div>

    <nav class="main-nav">
      <a class="nav-home" href="#">Home</a>
      <a class="nav-about" href="#">About us</a>
      <a class="nav-services" href="#">Our Services
        <svg width="14" height="9" viewBox="0 0 14 9" aria-hidden="true"><polyline points="1,1 7,7.5 13,1" fill="none" stroke="#0d2a3a" stroke-width="1.8"/></svg>
      </a>
      <a class="nav-contact" href="#">Contact</a>
    </nav>

    <h1 class="hero-title">OPTIMAL<br>RENEWABLE<br>VENTILATION</h1>
    <p class="hero-tagline">THE SOLUTION TO YOUR MAINTENANCE PROBLEM</p>

    <a class="btn btn-contact" href="#">Contact us</a>
    <a class="btn btn-services" href="#">Services</a>

    <div class="hero-photo" role="img" aria-label="Smiling technician in blue overalls holding a hard hat, standing in front of a range of air conditioning units"></div>
  </main>
</body>
</html>
```